Business Card Design Project

Hi I am after a business card double sided 1 side to have the attached PDF on front on the back:

Tavi Rundell - Managing Director
Mobile: 0412 638 274
email: tavi@pruvo.com.au
web: www.pruvo.com.au

Industry/Entity Type

Business

Font styles to use
Sans Serif

Requirements
Must have
• I want a classy looking card
Nice to have
• I like lime green and black and white

```html
<!DOCTYPE html>
<html lang="en">
<head>
<meta charset="utf-8">
<title>Pruvo Lawns and Gardens – Business Card</title>
<link rel="stylesheet" href="https://fonts.googleapis.com/css2?family=Open+Sans:wght@400;700&family=Questrial&display=swap">
<style>
  :root {
    --lime: #0cb80c;
    --lime-deep: #089a08;
    --ink: #231f1e;
    --paper: #ffffff;
    --stage: #e9ebe8;
    --muted: #333333;
  }
  * { box-sizing: border-box; margin: 0; padding: 0; }
  html, body {
    width: 1200px; height: 951px; overflow: hidden;
    background: var(--stage);
  }
  .canvas { position: relative; width: 1200px; height: 951px; }

  .card {
    position: absolute;
    width: 720px; height: 412px;
    border-radius: 24px;
    overflow: hidden;
    box-shadow: 0 6px 18px rgba(0,0,0,0.18);
    background: var(--paper);
  }

  /* Front side */
  .card-front { left: 90px; top: 50px; background: var(--lime); }
  .brand {
    position: absolute; left: 0; right: 0; top: 145px;
    display: flex; align-items: center; justify-content: center; gap: 18px;
  }
  .brand-mark {
    width: 46px; height: 46px;
    border: 3px solid var(--paper); border-radius: 6px;
  }
  .brand-name {
    font-family: "Questrial", sans-serif;
    font-size: 40px; color: var(--ink); letter-spacing: 0.5px;
  }
  .front-footer {
    position: absolute; left: 0; right: 0; bottom: 0; height: 62px;
    background: var(--paper);
    display: flex; align-items: center; justify-content: center;
    font-family: "Open Sans", sans-serif; font-size: 22px;
    color: var(--ink); letter-spacing: 1px;
  }

  /* Back side */
  .card-back { left: 390px; top: 500px; }
  .identity {
    position: absolute; left: 0; right: 0; top: 52px; text-align: center;
  }
  .person-name {
    font-family: "Open Sans", sans-serif; font-weight: 700;
    font-size: 38px; color: var(--lime); letter-spacing: 1px;
  }
  .person-role {
    font-family: "Open Sans", sans-serif; font-size: 18px;
    color: var(--muted); margin-top: 2px;
  }
  .band-top {
    position: absolute; left: 0; right: 0; top: 158px; height: 22px;
    background: var(--lime);
  }
  .band-web {
    position: absolute; left: 0; right: 0; top: 186px; height: 32px;
    background: var(--lime);
    display: flex; align-items: center; justify-content: center;
    font-family: "Open Sans", sans-serif; font-weight: 700;
    font-size: 18px; color: var(--paper); letter-spacing: 1px;
  }
  .contact-panel {
    position: absolute; left: 0; right: 0; top: 224px; bottom: 0;
    background: var(--ink);
  }
  .contact {
    position: absolute; top: 86px;
    display: flex; align-items: center; gap: 12px;
    font-family: "Open Sans", sans-serif; font-size: 20px;
    color: var(--paper); letter-spacing: 0.5px;
  }
  .contact-phone { left: 82px; }
  .contact-email { right: 48px; top: 104px; }
  .contact svg { fill: var(--lime); flex: none; }
</style>
</head>
<body>
<main class="canvas">

  <section class="card card-front" aria-label="Card front">
    <div class="brand">
      <span class="brand-mark"></span>
      <span class="brand-name">Pruvo Lawns and Gardens</span>
    </div>
    <div class="front-footer">www.pruvo.com.au</div>
  </section>

  <section class="card card-back" aria-label="Card back">
    <div class="identity">
      <h1 class="person-name">Tavi Rundell</h1>
      <p class="person-role">Managing Director</p>
    </div>
    <div class="band-top"></div>
    <div class="band-web">www.pruvo.com.au</div>
    <div class="contact-panel">
      <div class="contact contact-phone">
        <svg width="14" height="22" viewBox="0 0 14 22" aria-hidden="true">
          <rect x="0" y="0" width="14" height="22" rx="2"/>
          <rect x="2.5" y="3" width="9" height="11" fill="#231f1e"/>
        </svg>
        <span>0412 638 274</span>
      </div>
      <div class="contact contact-email">
        <svg width="20" height="14" viewBox="0 0 20 14" aria-hidden="true">
          <rect x="0" y="0" width="20" height="14" rx="1.5"/>
          <path d="M1 1 L10 8 L19 1" stroke="#231f1e" stroke-width="1.6" fill="none"/>
        </svg>
        <span>tavi@pruvo.com.au</span>
      </div>
    </div>
  </section>

</main>
</body>
</html>
```